Brightwire Hollow Business cards

one side I would like my logo (uploaded) and the other side I want my details. I'm an electrician in sydney. The logo side I'm happy with just a white background and our logo in the middle.

Details for other side
24/7 Sydney Electrician
Marcus Pell
0431 587 219
marcus@brightwirehollow.com.au
brightwirehollow.com.au
icons for facebook, instagram, linked in

Industry/Entity Type

electrician

Contact Information for Business Card

company info

```html
<!DOCTYPE html>
<html lang="en">
<head>
<meta charset="utf-8">
<title>Brightwire Hollow Business Cards</title>
<link rel="stylesheet" href="https://fonts.googleapis.com/css2?family=Exo+2:wght@500;600&family=Roboto+Condensed:wght@700&display=swap">
<style>
  :root {
    --stage: #2a2a2a;
    --brand-red: #ee3a24;
    --card-white: #f2f2f2;
    --ink: #3a3a3a;
    --white: #ffffff;
  }
  * { box-sizing: border-box; margin: 0; padding: 0; }
  html, body { width: 1200px; height: 1200px; overflow: hidden; }
  body {
    background: var(--stage);
    font-family: "Exo 2", sans-serif;
    position: relative;
  }
  .card {
    position: absolute;
    top: 229px;
    width: 424px;
    height: 742px;
    box-shadow: 0 10px 30px rgba(0,0,0,0.45);
  }
  .card--logo { left: 152px; background: var(--brand-red); }
  .card--details { left: 624px; background: var(--card-white); }

  .wordmark {
    position: absolute;
    left: 0; right: 0;
    text-align: center;
    font-weight: 600;
    text-transform: uppercase;
    line-height: 1;
  }
  .wordmark__main { display: block; font-size: 44px; letter-spacing: 1px; }
  .wordmark__sub { display: block; font-size: 30px; letter-spacing: 22px; margin-top: 8px; padding-left: 22px; }
  .card--logo .wordmark { top: 318px; color: var(--white); }
  .card--details .wordmark { top: 64px; color: var(--ink); }
  .card--details .wordmark__main { font-size: 40px; }
  .card--details .wordmark__sub { font-size: 27px; letter-spacing: 20px; padding-left: 20px; }

  .contact-band {
    position: absolute;
    top: 174px;
    left: 0; right: 0;
    height: 230px;
    background: var(--brand-red);
    color: var(--white);
    text-align: center;
    padding-top: 22px;
  }
  .person__name { font-size: 33px; font-weight: 500; line-height: 1.1; letter-spacing: 0.5px; }
  .person__phone { font-size: 37px; font-weight: 500; line-height: 1.1; letter-spacing: 1.5px; }
  .contact-band__divider {
    width: 238px; height: 2px;
    background: var(--white);
    margin: 12px auto 14px;
  }

  .links {
    position: absolute;
    top: 452px; left: 0; right: 0;
    display: flex; flex-direction: column; align-items: center; gap: 6px;
    font-size: 15px; color: var(--ink);
  }
  .links__item { display: flex; align-items: center; gap: 7px; }
  .links__item svg { width: 14px; height: 14px; }
  .social {
    position: absolute;
    top: 518px; left: 0; right: 0;
    display: flex; justify-content: center; gap: 10px;
  }
  .social__dot { width: 14px; height: 14px; border-radius: 50%; background: var(--brand-red); }

  .tagline {
    position: absolute;
    top: 596px; left: 0; right: 0;
    text-align: center;
    font-family: "Roboto Condensed", sans-serif;
    font-weight: 700;
    font-size: 27px;
    color: var(--brand-red);
  }
  .wire-rule { position: absolute; top: 648px; left: 44px; width: 336px; height: 36px; }
</style>
</head>
<body>
  <section class="card card--logo" aria-label="Business card front">
    <div class="wordmark">
      <span class="wordmark__main">Brightwire</span>
      <span class="wordmark__sub">Hollow</span>
    </div>
  </section>

  <section class="card card--details" aria-label="Business card back">
    <div class="wordmark">
      <span class="wordmark__main">Brightwire</span>
      <span class="wordmark__sub">Hollow</span>
    </div>

    <div class="contact-band">
      <div class="person">
        <p class="person__name">Marcus Pell</p>
        <p class="person__phone">0431 587 219</p>
      </div>
      <div class="contact-band__divider"></div>
      <div class="person">
        <p class="person__name">Owen Castell</p>
        <p class="person__phone">0452 318 760</p>
      </div>
    </div>

    <div class="links">
      <p class="links__item">
        <svg viewBox="0 0 14 14" aria-hidden="true"><rect x="1" y="3" width="12" height="8" fill="#3a3a3a"/><path d="M1 3 L7 8 L13 3" stroke="#ee3a24" stroke-width="1.4" fill="none"/></svg>
        services@brightwirehollow.com.au
      </p>
      <p class="links__item">
        <svg viewBox="0 0 14 14" aria-hidden="true"><circle cx="7" cy="7" r="5.5" fill="none" stroke="#3a3a3a" stroke-width="1.3"/><ellipse cx="7" cy="7" rx="2.3" ry="5.5" fill="none" stroke="#3a3a3a" stroke-width="1.1"/><line x1="1.5" y1="7" x2="12.5" y2="7" stroke="#3a3a3a" stroke-width="1.1"/></svg>
        brightwirehollow.com.au
      </p>
    </div>

    <div class="social" aria-label="Social media">
      <span class="social__dot"></span>
      <span class="social__dot"></span>
    </div>

    <p class="tagline">24/7 SYDNEY ELECTRICIANS</p>

    <svg class="wire-rule" viewBox="0 0 336 36" aria-hidden="true">
      <rect x="0" y="6" width="336" height="3" fill="#ee3a24"/>
      <rect x="87" y="2" width="130" height="11" fill="#ee3a24"/>
      <rect x="0" y="26" width="336" height="3" fill="#ee3a24"/>
    </svg>
  </section>
</body>
</html>
```